Jewelry Wholesale Business Card Design

Company name: VELORA
Business Background: Wholesale jewelry store located in downtown Los Angeles. We specialize in 18k gold-filled, stainless steel, 14kt gold, and natural stone jewelry.
website: www.velorashop.example
Instagram: velora_
Email: sales@velorashop.example
Address: 318 W. PRIOR ST #27, #109
LOS ANGELES, CA 90099
(213)555-0147

We would like to create a simple, yet elegant business card for my store
-Includes company logo
-Black background preferred
-Gold metallic color letters
- Lists the type of products we sell
-Small icons for instagram handle, phone, email, and website

Target Market(s)

Hispanic community, age 12-40

Industry/Entity Type

Jewelry Wholesale

Contact Information for Business Card

logo, business location, website, phone number, email, instagram, lists type of products, Dylan Morvet(my name)

Font styles to use
Serif
Sans Serif

Colors
FFF300
FFF600
FEFA6F
FFFEC7
FFFEE8

Requirements
Must have
• logo, business location, website, phone number, email, instagram, lists type of products, Dylan Morvet(my name)

```html
<!DOCTYPE html>
<html lang="en">
<head>
<meta charset="utf-8">
<title>VELORA Business Card</title>
<link rel="stylesheet" href="https://fonts.googleapis.com/css2?family=Montserrat:wght@400;500;600&display=swap">
<style>
  :root {
    --backdrop: #3a3a3a;
    --card-black: #141414;
    --card-edge: #c9a24e;
    --gold: #d8b25e;
    --gold-soft: #c9a455;
    --pattern-dark: #0b0b0b;
    --pattern-light: #2a2a2a;
  }
  * { box-sizing: border-box; margin: 0; padding: 0; }
  html, body {
    width: 1200px; height: 801px; overflow: hidden;
    background: var(--backdrop);
    font-family: "Montserrat", Arial, sans-serif;
  }
  .stage {
    width: 1200px; height: 801px;
    display: flex; align-items: center; justify-content: center; gap: 60px;
  }
  .card {
    position: relative;
    width: 520px; height: 297px;
    background: var(--card-black);
    border: 2px solid var(--card-edge);
    box-shadow: 0 14px 30px rgba(0,0,0,.45);
    overflow: hidden;
  }
  .brand-name {
    position: absolute; left: 40px; top: 128px;
    font-size: 40px; font-weight: 600; letter-spacing: 3px;
    color: var(--gold);
  }
  .divider {
    position: absolute; left: 262px; top: 58px;
    width: 1px; height: 126px; background: var(--gold-soft);
  }
  .contact {
    position: absolute; left: 282px; top: 52px;
    color: var(--gold); font-size: 12px; font-weight: 500; line-height: 19px;
    list-style: none;
  }
  .contact li { display: flex; align-items: center; gap: 7px; white-space: nowrap; }
  .contact .address { padding-left: 0; }
  .contact svg { width: 11px; height: 11px; flex: none; fill: var(--gold); }
  .owner { margin-top: 4px; font-weight: 600; letter-spacing: .5px; }
  .products {
    position: absolute; left: 0; right: 0; bottom: 26px;
    text-align: center; color: var(--gold);
    font-size: 13px; font-weight: 500; letter-spacing: .3px;
  }
  .card-back { background: var(--card-black); }
  .pattern-field {
    position: absolute; inset: 0;
    background: linear-gradient(120deg, var(--pattern-dark) 0%, #1a1a1a 55%, var(--pattern-light) 100%);
  }
  .back-mark {
    position: absolute; right: 44px; top: 118px;
    font-size: 18px; font-weight: 600; letter-spacing: 2px;
    color: var(--gold);
  }
</style>
</head>
<body>
<main class="stage">
  <section class="card card-front" aria-label="Card front">
    <div class="brand-name">VELORA</div>
    <div class="divider"></div>
    <ul class="contact">
      <li class="address">318 W. PRIOR ST #27, #109</li>
      <li class="address">LOS ANGELES, CA 90099</li>
      <li>
        <svg viewBox="0 0 12 12" aria-hidden="true"><path d="M2.5 1h2l1 3-1.3 1a6 6 0 0 0 2.8 2.8l1-1.3 3 1v2c0 .6-.5 1.5-1.5 1.5A9.5 9.5 0 0 1 1 2.5C1 1.5 1.9 1 2.5 1z"/></svg>
        (213)555-0147
      </li>
      <li>
        <svg viewBox="0 0 12 12" aria-hidden="true"><path d="M1 3h10v6.5H1z M1 3l5 3.5L11 3" fill="none" stroke="#d8b25e" stroke-width="1.3"/></svg>
        sales@velorashop.example
      </li>
      <li>
        <svg viewBox="0 0 12 12" aria-hidden="true"><g fill="none" stroke="#d8b25e" stroke-width="1.1"><circle cx="6" cy="6" r="5"/><ellipse cx="6" cy="6" rx="2.2" ry="5"/><path d="M1 6h10"/></g></svg>
        www.velorashop.example
      </li>
      <li>
        <svg viewBox="0 0 12 12" aria-hidden="true"><rect x="1" y="1" width="10" height="10" rx="2" fill="none" stroke="#d8b25e" stroke-width="1.3"/></svg>
        velora_
      </li>
      <li class="owner">Dylan Morvet</li>
    </ul>
    <p class="products">18k gold-filled &bull; stainless steel &bull; 14kt gold &bull; and natural stone jewelry</p>
  </section>

  <section class="card card-back" aria-label="Card back">
    <div class="pattern-field" role="img" aria-label="Repeating tone-on-tone gloss pattern of the brand initial across the black card"></div>
    <div class="back-mark">VELORA</div>
  </section>
</main>
</body>
</html>
```